Design Creative Banner or Gif Ads. 3 Designs To Be Selected

Come up with some creative banner ads for stonewell.co.nz

*At least 3 different winning banners will be chosen*

Please provide banner ads / gif ads in common google ads / website banner formats.

They can be gif or static but must stand out while still maintaining clear clean text and visuals, with a premium professional feel (please avoid clip art or anything that gives a cheap message).

Please keep in mind that these will likely be small ads so text needs to be large and if there's there a lot of text then use multiple frames/ pages as submit as a gif.

Style
Minimal & clean lines
Architectural or realistic images
Avoid cartoon styles, clipart, or anything that looks cheap

Font
Nexa or Montserrat or similar

Tone
Premium, serious, trustworthy — fits new builds

Colours
Option 1: Deep Navy (trust & quality) & lighter blues and warm grey
Option 2: Open to bright colours to help the ads stand out, such as (but not limited to) bright pink with black, yellow, fluorescent green, provided the messaging is still done professionally.
Our logo is attached (Stone Well Logo)

Display Sizes
Ad specs for file sizes should be file formats like JPEG, GIF, and PNG, with animations limited to a max of 30 seconds or less.
We will need several different ad sizes provided for each of the 3 selected winning designs.

• Medium Rectangle: 300 × 250 pixels
• Leaderboard: 728 × 90 pixels
• Desktop Banner ad image: (640x360 pixels)
• Desktop Banner ad image 2: (300x600 pixels)
• Possibly one or two other sizes

Flexibility to be creative
The ad text, words, upper/lower case, layout, colour, theme, and images can be adjusted to how you think it will look best. The follow example ads are just examples of what we are after but we are keen to see what you can create.

Recommendations at this point:
1. Avoid text heavy
2. Looking for more Gif ads
3. Imaging: if possible use real stock photo's rather than AI

Themes:

1
Building Soon? Start Here
Free Build Planning Pack:
✓ Build Cost Calculator
✓ Hidden Cost Checklist
✓ Builder Comparison Guide
Build With Confidence
Download Free

2
Before You Choose A Builder
Compare Price, Scope, Risk & Value
Avoid Costly Mistakes
Choose The Right Builder With Confidence
Download The Free Guide

3
Planning A New Build?
Avoid These Common Mistakes:
✗ Hidden Exclusions
✗ Missing Scope
✗ Unrealistic Allowances
✗ Budget Blowouts
Download The Free Guide

4
Before You Buy Land
Know what it could cost to build.
Avoid Costly Building Mistakes
Download Our Free Guides

5
Know Your Build Budget?
• Free Build Cost Calculator
• Hidden Cost Checklist
• Build Planning Tools
Calculate Costs (Download)

Target Market(s)

Landowners looking to build

Industry/Entity Type

Building

Font styles to use
Other font styles liked:
• Nexa or Montserrat or similar

Requirements
Should not have
• Avoid cartoon styles, clipart, or anything that looks cheap

```html
<!DOCTYPE html>
<html lang="en">
<head>
<meta charset="utf-8">
<title>Stone Well – Animated GIF Banner Ad Storyboard</title>
<link rel="stylesheet" href="https://fonts.googleapis.com/css2?family=Montserrat:wght@400;500;600;700;800&display=swap">
<style>
  :root{
    --navy:#1b3658;
    --navy-deep:#0f2744;
    --sky:#2e8fc1;
    --badge:#1f6fb8;
    --ink:#1c2b3d;
    --muted:#5b6675;
    --green:#2a9a3e;
    --orange:#f08a1c;
    --red:#e0262a;
    --slate:#5a7190;
    --g-green:#4aa844;
    --g-blue:#5d7a9e;
    --g-yellow:#f5b731;
    --g-orange:#f28b30;
    --g-red:#e8412c;
    --panel-top:#ffffff;
    --panel-bottom:#9cb6d3;
    --loop-bg:#f4f5f7;
    --button:#1e6fa8;
  }
  *{margin:0;padding:0;box-sizing:border-box}
  html,body{width:1200px;height:563px;overflow:hidden;background:#fff}
  body{font-family:"Montserrat",sans-serif;color:var(--ink);position:relative}

  .brand{position:absolute;display:flex;align-items:center;gap:6px;font-weight:700;color:var(--navy);white-space:nowrap}
  .brand-square{background:var(--navy)}
  .brand--page{left:29px;top:15px;font-size:20px;gap:9px}
  .brand--page .brand-square{width:30px;height:30px}

  .page-title{position:absolute;left:0;right:0;top:14px;padding-left:14px;text-align:center;font-size:47px;font-weight:800;color:var(--navy);letter-spacing:0.5px}
  .page-subtitle{position:absolute;left:0;right:0;top:84px;text-align:center;font-size:20px;font-weight:500;color:var(--ink);padding-left:0}

  .frame{position:absolute;top:141px;width:141px;height:282px;overflow:hidden;
    background:linear-gradient(180deg,var(--panel-top) 0%,#f1f4f8 45%,var(--panel-bottom) 100%)}
  .frame .brand{left:0;right:0;justify-content:center;top:8px;font-size:6.5px;gap:3px}
  .frame .brand-square{width:8px;height:8px}
  .eyebrow{position:absolute;left:0;right:0;top:31px;text-align:center;font-size:5.6px;font-weight:800;letter-spacing:1.1px;color:var(--navy)}
  .headline{position:absolute;left:0;right:0;top:43px;text-align:center;font-size:13.6px;line-height:14px;font-weight:800;color:var(--navy)}
  .lede{position:absolute;left:10px;right:10px;top:77px;text-align:center;font-size:6.6px;line-height:9px;color:var(--muted)}
  .gauge{position:absolute;left:12px;top:104px;width:116px;height:83.5px}
  .scale-label{position:absolute;top:174px;font-size:4.6px;font-weight:800;color:var(--navy)}
  .scale-label--min{left:25px}
  .scale-label--max{left:106px}
  .budget-label{position:absolute;left:0;right:0;top:187px;text-align:center;font-size:5.6px;font-weight:800;letter-spacing:1.6px;color:var(--muted)}
  .budget{position:absolute;left:0;right:0;top:196px;height:26px;overflow:hidden;text-align:center;font-size:18.5px;font-weight:800}
  .budget span{display:block;line-height:24px}
  .budget--green{color:var(--green)}
  .budget--orange{color:var(--orange)}
  .budget--red{color:var(--red);top:201px;font-size:19px}
  .budget--rolling{top:198px}
  .budget--rolling .outgoing{color:var(--navy);margin-top:-18px;opacity:.9}
  .budget--rolling .incoming{color:var(--slate);margin-top:-5px}
  .footnote{position:absolute;left:0;right:0;top:249px;text-align:center;font-size:6.2px;line-height:8.5px;font-weight:700;color:var(--ink)}

  .frame--intro{background:none}
  .intro-art{position:absolute;inset:0;background:linear-gradient(160deg,#1e4270 0%,#15325a 45%,var(--navy-deep) 100%)}
  .frame--intro .brand{top:64px;color:#fff}
  .frame--intro .brand-square{background:#fff}
  .frame--intro .eyebrow{top:90px;color:#5fb0e0;font-size:6px}
  .frame--intro .headline{top:113px;font-size:17px;line-height:19.5px;color:#c9d3df}

  .frame--offer .brand{top:17px;font-size:7px}
  .guide-cover{position:absolute;left:34px;top:46px;width:72px;height:107px;border-radius:2px;
    background:linear-gradient(135deg,#6f9ccb 0%,#4c7fb5 55%,#3a6aa0 100%);box-shadow:0 4px 8px rgba(15,39,68,.25)}
  .offer-title{position:absolute;left:0;right:0;top:166px;text-align:center;font-size:15px;line-height:16.3px;font-weight:800;color:var(--navy)}
  .offer-copy{position:absolute;left:8px;right:8px;top:223px;text-align:center;font-size:7.4px;line-height:10.5px;color:var(--muted)}
  .cta{position:absolute;left:13px;width:116px;top:257px;height:20px;border-radius:2px;background:var(--button);color:#fff;
    font-size:6.4px;font-weight:800;letter-spacing:.6px;display:flex;align-items:center;justify-content:center}

  .frame--loop{background:var(--loop-bg)}
  .loop-ring{position:absolute;left:20px;top:95px;width:96px;height:96px}
  .loop-text{position:absolute;left:0;width:137px;top:129px;text-align:center;font-size:13px;line-height:15px;font-weight:800;color:var(--navy)}

  .step{position:absolute;top:440px;width:30px;height:30px}
  .step svg{display:block}
  .step b{position:absolute;left:0;width:24px;top:4px;text-align:center;color:#fff;font-size:19px;font-weight:700}

  .about-heading{position:absolute;left:22px;top:513px;font-size:29px;font-weight:500;color:var(--sky)}
  .about-copy{position:absolute;left:280px;top:513px;font-size:15px;line-height:17.5px;font-weight:500;color:var(--sky)}
</style>
</head>
<body>

<svg width="0" height="0" style="position:absolute" aria-hidden="true">
  <defs>
    <symbol id="gauge-dial" viewBox="0 0 100 72">
      <g fill="none" stroke-width="9">
        <path d="M12.4 63.7 A40 40 0 0 1 12.4 36.3" stroke="var(--g-green)"/>
        <path d="M12.4 36.3 A40 40 0 0 1 27.1 17.2" stroke="var(--g-blue)"/>
        <path d="M27.1 17.2 A40 40 0 0 1 50 10" stroke="var(--g-blue)"/>
        <path d="M50 10 A40 40 0 0 1 72.9 17.2" stroke="var(--g-blue)"/>
        <path d="M72.9 17.2 A40 40 0 0 1 84.6 30" stroke="var(--g-yellow)"/>
        <path d="M84.6 30 A40 40 0 0 1 90 50" stroke="var(--g-orange)"/>
        <path d="M90 50 A40 40 0 0 1 87.6 63.7" stroke="var(--g-red)"/>
      </g>
      <g stroke="#fff" stroke-width="0.8">
        <line x1="4" y1="36.3" x2="20" y2="36.3" transform="rotate(0)"/>
      </g>
      <path d="M21.8 60.3 A30 30 0 1 1 78.2 60.3" fill="none" stroke="#9aa6b4" stroke-width="1.6" stroke-dasharray="0.6 3.6"/>
    </symbol>
  </defs>
</svg>

<div class="brand brand--page"><span class="brand-square"></span>Stone Well</div>
<h1 class="page-title">ANIMATED GIF BANNER AD</h1>
<p class="page-subtitle">300 x 600 web banner storyboard</p>

<!-- Frame 1: intro -->
<section class="frame frame--intro" style="left:13px">
  <div class="intro-art" role="img" aria-label="Dark navy architectural house drawing in the background"></div>
  <div class="brand"><span class="brand-square"></span>Stone Well</div>
  <p class="eyebrow">BUILD COST CHECK</p>
  <h2 class="headline">Planning A<br>New<br>Build?</h2>
</section>

<!-- Frame 2 -->
<section class="frame" style="left:187px">
  <div class="brand"><span class="brand-square"></span>Stone Well</div>
  <p class="eyebrow">BUILD COST CHECK</p>
  <h2 class="headline">Planning A New<br>Build?</h2>
  <p class="lede">Know your costs before you commit.</p>
  <svg class="gauge" viewBox="0 0 100 72"><use href="#gauge-dial"/>
    <polygon points="50,47.8 83,50 50,52.2" fill="var(--navy)" transform="rotate(-195 50 50)"/>
    <circle cx="50" cy="50" r="5" fill="#fff" stroke="var(--navy)" stroke-width="2.2"/></svg>
  <span class="scale-label scale-label--min">MIN</span><span class="scale-label scale-label--max">MAX</span>
  <p class="budget-label">BUDGET</p>
  <p class="budget budget--green"><span>$750,000</span></p>
  <p class="footnote">Compare price, scope,<br>risk &amp; value before you sign.</p>
</section>

<!-- Frame 3 -->
<section class="frame" style="left:361px">
  <div class="brand"><span class="brand-square"></span>Stone Well</div>
  <p class="eyebrow">BUILD COST CHECK</p>
  <h2 class="headline">Planning A New<br>Build?</h2>
  <p class="lede">Know your costs before you commit.</p>
  <svg class="gauge" viewBox="0 0 100 72"><use href="#gauge-dial"/>
    <polygon points="50,47.8 83,50 50,52.2" fill="var(--navy)" transform="rotate(-152 50 50)"/>
    <circle cx="50" cy="50" r="5" fill="#fff" stroke="var(--navy)" stroke-width="2.2"/></svg>
  <span class="scale-label scale-label--min">MIN</span><span class="scale-label scale-label--max">MAX</span>
  <p class="budget-label">BUDGET</p>
  <p class="budget budget--rolling"><span class="outgoing">$750,000</span><span class="incoming">$900,000</span></p>
  <p class="footnote">Compare price, scope,<br>risk &amp; value before you sign.</p>
</section>

<!-- Frame 4 -->
<section class="frame" style="left:536px">
  <div class="brand"><span class="brand-square"></span>Stone Well</div>
  <p class="eyebrow">BUILD COST CHECK</p>
  <h2 class="headline">Planning A New<br>Build?</h2>
  <p class="lede">Know your costs before you commit.</p>
  <svg class="gauge" viewBox="0 0 100 72"><use href="#gauge-dial"/>
    <polygon points="50,47.8 83,50 50,52.2" fill="var(--navy)" transform="rotate(-56 50 50)"/>
    <circle cx="50" cy="50" r="5" fill="#fff" stroke="var(--navy)" stroke-width="2.2"/></svg>
  <span class="scale-label scale-label--min">MIN</span><span class="scale-label scale-label--max">MAX</span>
  <p class="budget-label">BUDGET</p>
  <p class="budget budget--orange"><span>$1,100,000</span></p>
  <p class="footnote">Compare price, scope,<br>risk &amp; value before you sign.</p>
</section>

<!-- Frame 5 -->
<section class="frame" style="left:710px">
  <div class="brand"><span class="brand-square"></span>Stone Well</div>
  <p class="eyebrow">BUILD COST CHECK</p>
  <h2 class="headline">Planning A New<br>Build?</h2>
  <p class="lede">Know your costs before you commit.</p>
  <svg class="gauge" viewBox="0 0 100 72"><use href="#gauge-dial"/>
    <polygon points="50,47.8 84,50 50,52.2" fill="var(--navy)" transform="rotate(4 50 50)"/>
    <circle cx="50" cy="50" r="5" fill="#fff" stroke="var(--navy)" stroke-width="2.2"/></svg>
  <span class="scale-label scale-label--min">MIN</span><span class="scale-label scale-label--max">MAX</span>
  <p class="budget-label">BUDGET</p>
  <p class="budget budget--red"><span>$1,300,000</span></p>
  <p class="footnote">Compare price, scope,<br>risk &amp; value before you sign.</p>
</section>

<!-- Frame 6: offer -->
<section class="frame frame--offer" style="left:878px">
  <div class="brand"><span class="brand-square"></span>Stone Well</div>
  <div class="guide-cover" role="img" aria-label="Printed planning guide booklet in blue"></div>
  <h2 class="offer-title">Free Build<br>Planning<br>Guides</h2>
  <p class="offer-copy">Compare builders on price,<br>scope, risk &amp; value.</p>
  <div class="cta">DOWNLOAD FREE GUIDE</div>
</section>

<!-- Frame 7: loop -->
<section class="frame frame--loop" style="left:1045px">
  <svg class="loop-ring" viewBox="0 0 96 96" aria-hidden="true">
    <circle cx="48" cy="48" r="45" fill="none" stroke="var(--navy)" stroke-width="1" stroke-dasharray="3 3"/>
    <polygon points="89,42 97,42 93,49" fill="var(--navy)"/>
  </svg>
  <p class="loop-text">LOOP<br>RESTARTS</p>
</section>

<!-- Step markers -->
<div class="step" style="left:69px"><svg width="30" height="30"><polygon points="0,0 24,0 30,15 24,30 0,30" fill="var(--badge)"/></svg><b>1</b></div>
<div class="step" style="left:243px"><svg width="30" height="30"><polygon points="0,0 24,0 30,15 24,30 0,30" fill="var(--badge)"/></svg><b>2</b></div>
<div class="step" style="left:413px"><svg width="30" height="30"><polygon points="0,0 24,0 30,15 24,30 0,30" fill="var(--badge)"/></svg><b>3</b></div>
<div class="step" style="left:592px"><svg width="30" height="30"><polygon points="0,0 24,0 30,15 24,30 0,30" fill="var(--badge)"/></svg><b>4</b></div>
<div class="step" style="left:762px"><svg width="30" height="30"><polygon points="0,0 24,0 30,15 24,30 0,30" fill="var(--badge)"/></svg><b>5</b></div>
<div class="step" style="left:926px"><svg width="30" height="30"><polygon points="0,0 24,0 30,15 24,30 0,30" fill="var(--badge)"/></svg><b>6</b></div>
<div class="step" style="left:1104px"><svg width="30" height="30"><polygon points="0,0 24,0 30,15 24,30 0,30" fill="var(--badge)"/></svg><b>7</b></div>

<h2 class="about-heading">ABOUT THIS AD</h2>
<p class="about-copy">This is an animated GIF (motion) banner ad<br>designed for web&nbsp;&nbsp; placements.</p>

</body>
</html>
```